New Design for Brightcoilheat [Zimpla]

Hello, This is my 2nd project here. I need a new web design for www.brightcoilheat.com.au which is one of my clients, and an extremely outdated website. It only has a few links and is fairly straight forward, looking for a more professional, up-to-date looking website. Please note: The website will be made under a zimpla white-label platform, so the design MUST be consistent with this type of platform. Many more projects will be up and coming so the best designers will definitely be selected for future projects.
Thankyou

• Please refer to www.brightcoilheat.com.au to find all the content.

```html
<!DOCTYPE html>
<html lang="en">
<head>
<meta charset="utf-8">
<title>Brightcoilheat – Thermal and Sealing Specialists</title>
<link rel="stylesheet" href="https://fonts.googleapis.com/css2?family=Arimo:wght@400;700&family=Oswald:wght@300;400&family=Questrial&display=swap">
<style>
:root{
  --page:#f3f3f3;
  --band-top:#e4e4e4;
  --band-bottom:#d9d9d9;
  --white:#ffffff;
  --ink:#222222;
  --text:#555555;
  --muted:#777777;
  --line:#d4d4d4;
  --panel:#f7f7f7;
  --dark:#202020;
  --nav-active:#4a4a4a;
}
*{box-sizing:border-box;margin:0;padding:0}
html,body{width:956px;height:1200px;overflow:hidden}
body{position:relative;background:var(--page);font-family:"Arimo",Arial,sans-serif;color:var(--text)}
.abs{position:absolute}
.header-band{left:0;top:0;width:956px;height:174px;border-top:3px solid #555;
  background:repeating-linear-gradient(90deg,rgba(255,255,255,.25) 0 1px,transparent 1px 3px),linear-gradient(var(--band-top),var(--band-bottom))}
.brand{left:151px;top:19px;display:flex;align-items:flex-end;gap:8px}
.brand-mark{width:78px;height:78px;background:var(--dark);border:4px solid #c9c9c9;outline:1px solid #999}
.brand-name{font-size:11px;color:var(--ink);padding-bottom:2px;letter-spacing:.2px}
.contact-info{right:151px;top:39px;text-align:right;font-size:9.5px;line-height:24px;color:var(--text)}
.contact-info b{color:var(--ink);font-weight:700;margin-right:4px}
.contact-info .sep{margin:0 8px;color:#888}
.sheet{left:150px;top:119px;width:656px;height:1028px;background:var(--white);border:1px solid #d0d0d0}
.nav-item{top:128px;height:45px;line-height:45px;text-align:center;font-size:13px;color:var(--ink);text-transform:uppercase}
.nav-item.active{background:var(--nav-active);color:var(--white)}
.nav-sep{top:130px;height:41px;border-left:1px dotted #c8c8c8}
.banner{left:159px;top:183px;width:638px;height:238px;background:linear-gradient(#e9e9e9,#fdfdfd 60%)}
.banner-copy{left:170px;top:238px;width:300px;text-align:center;font-family:"Oswald",sans-serif;font-weight:300;font-size:21px;line-height:31px;color:var(--ink)}
.banner-art{left:478px;top:189px;width:318px;height:228px;border-radius:6px;
  background:radial-gradient(ellipse at 40% 40%,#6fbf3f 0,#4ca23a 25%,rgba(90,170,230,.7) 45%,rgba(210,210,210,.6) 70%,transparent 85%)}
.dots{left:268px;top:405px;display:flex;gap:9px}
.dots span{width:8px;height:8px;border-radius:50%;background:#ccc}
.dots span.on{background:#444}
.rule{left:159px;width:638px;height:1px;background:var(--line);box-shadow:0 3px 4px rgba(0,0,0,.06)}
.welcome{left:159px;top:457px;width:221px;height:194px;background:var(--dark);padding:10px}
.welcome-inner{height:100%;border:1px dotted #666;padding:22px 20px 0 20px;color:var(--white)}
.welcome h2{font-family:"Questrial",sans-serif;font-weight:400;font-size:20px;margin-bottom:13px}
.welcome p{font-size:9.5px;line-height:15px;color:#eee}
.specialists{left:391px;top:457px;width:406px;height:194px;border-top:1px solid #e6e6e6;border-bottom:1px solid #e6e6e6}
h3{font-family:"Questrial",sans-serif;font-weight:400;font-size:16px;color:var(--ink)}
.specialists h3{position:absolute;left:11px;top:10px}
.chev-list{list-style:none;font-size:8.5px;color:var(--text)}
.chev-list li{position:relative;padding-left:14px;line-height:12px;margin-bottom:6.4px}
.chev-list li::before{content:"›";position:absolute;left:1px;top:-1px;font-size:11px;color:#888}
.spec-a{left:405px;top:496px;width:200px}
.spec-b{left:616px;top:496px;width:180px}
.panel{background:var(--panel);border:1px solid #e2e2e2}
.products{left:159px;top:672px;width:408px;height:336px}
.products h3{position:absolute;left:17px;top:12px}
.photo{top:722px;width:154px;height:121px;border:1px solid #ccc;background:#eee;padding:6px}
.photo div{width:100%;height:100%;background:linear-gradient(135deg,#bdbdbd,#5a5a5a 55%,#2c2c2c)}
.photo.b div{background:radial-gradient(circle at 35% 45%,#e8e8e8 0,#b5b5b5 30%,#4a4a4a 75%)}
.prod-a{left:178px;top:861px;width:180px}
.prod-b{left:392px;top:861px;width:170px}
.prod-a li,.prod-b li{margin-bottom:7.4px}
.profile{left:578px;top:672px;width:219px;height:185px}
.profile h3{position:absolute;left:16px;top:12px}
.dot-list{list-style:none;font-size:9.5px;color:var(--ink)}
.dot-list li{position:relative;padding-left:8px;line-height:18.5px}
.dot-list li::before{content:"";position:absolute;left:0;top:7px;border:2.5px solid transparent;border-left:3px solid #444}
.prof-a{left:595px;top:716px}
.prof-b{left:698px;top:716px}
.testimonial{left:578px;top:868px;width:219px;height:140px}
.testimonial h3{position:absolute;left:16px;top:12px}
.testimonial p{position:absolute;left:17px;top:42px;width:190px;font-size:9.5px;line-height:15px;color:var(--ink)}
.testimonial a{position:absolute;left:17px;top:116px;font-size:9px;font-weight:700;color:var(--ink);text-decoration:none}
.footer-links{left:150px;top:1046px;width:656px;text-align:center;font-size:9.5px;color:var(--muted)}
.footer-links a{color:var(--muted);text-decoration:none;margin:0 12px}
.footer-links a.current{color:var(--ink)}
.footer-links .bar{color:#999}
.footer-note{left:150px;width:656px;text-align:center;font-size:9.5px;color:var(--muted)}
.footer-note.small{font-size:8.8px}
.social{display:inline-block;width:10px;height:10px;border-radius:50%;background:#aaa;vertical-align:-1px;margin-left:4px}
</style>
</head>
<body>
<div class="abs header-band"></div>

<div class="abs brand">
  <div class="brand-mark"></div>
  <div class="brand-name">BRIGHTCOILHEAT</div>
</div>

<div class="abs contact-info">
  <div><b>PHONE :</b>+61 3 5550 1427<span class="sep">|</span><b>FAX :</b>+61 3 5550 1432</div>
  <div><b>EMAIL :</b>sales@brightcoilheat.com.au</div>
  <div><b>CONTACT :</b>Alan Pryor - Dean Pryor</div>
</div>

<div class="abs sheet"></div>

<nav>
  <div class="abs nav-item active" style="left:159px;width:78px">Home</div>
  <div class="abs nav-sep" style="left:240px"></div>
  <div class="abs nav-item" style="left:244px;width:105px">Services</div>
  <div class="abs nav-sep" style="left:349px"></div>
  <div class="abs nav-item" style="left:351px;width:107px">Product</div>
  <div class="abs nav-sep" style="left:458px"></div>
  <div class="abs nav-item" style="left:460px;width:103px">Aboutus</div>
  <div class="abs nav-sep" style="left:563px"></div>
  <div class="abs nav-item" style="left:565px;width:121px">Contactus</div>
  <div class="abs nav-sep" style="left:686px"></div>
  <div class="abs nav-item" style="left:688px;width:122px">Partners</div>
</nav>

<section>
  <div class="abs banner"></div>
  <div class="abs banner-copy">The experience, knowledge and facility to design and fabricate gives you the quality Australian made products you demand.</div>
  <div class="abs banner-art" role="img" aria-label="Illustration of a green house shape with blue airflow arrows over building plans, with two workers in silhouette and a measuring rule"></div>
  <div class="abs dots"><span class="on"></span><span></span><span></span><span></span></div>
</section>

<div class="abs rule" style="top:434px"></div>

<section class="abs welcome">
  <div class="welcome-inner">
    <h2>Welcome!</h2>
    <p>Brightcoilheat are one of Australia's leading suppliers and manufacturers of thermal fabrics and fabrications. The experience, know­ledge and facility to design and fabri­cate gives you the quality Australian made products you demand.</p>
  </div>
</section>

<section class="abs specialists"><h3>Thermal and Sealing Specialists</h3></section>
<ul class="abs chev-list spec-a">
  <li>Thermal Fabrics and Fabrications</li>
  <li>High and Low Temperature Insulation</li>
  <li>Furnace / Oven Door Seals</li>
  <li>Welding Blankets and Curtains</li>
  <li>Fabric Expansion Joints</li>
  <li>Boat Exhaust Covers</li>
  <li>Thermal Hoods / Covers</li>
</ul>
<ul class="abs chev-list spec-b">
  <li>Acoustic Materials</li>
  <li>Pump and Valve Packings</li>
  <li>Gasket Materials</li>
  <li>Standard and Non-Standard Gaskets</li>
  <li>Boilers Gaskets and Seals</li>
  <li>Spiral Wounds</li>
  <li>Bright Seal</li>
  <li>and Lots more</li>
</ul>

<section class="abs panel products"><h3>Thermal Product available at Brightcoilheat</h3></section>
<div class="abs photo" style="left:178px"><div role="img" aria-label="Photo of a fabricated stainless thermal hood"></div></div>
<div class="abs photo b" style="left:393px"><div role="img" aria-label="Photo of a tub of sealant beside rolls of ceramic fibre rope"></div></div>
<ul class="abs chev-list prod-a">
  <li>Ceramic Fibre Tapes, Ropes,<br>Braids, Boards &amp; Insulation.</li>
  <li>Glass Fibre Tapes, Ropes,<br>Braids, Boards &amp; Insulation.</li>
  <li>Furnace / Oven Tadpole Tape Seals.</li>
  <li>Boiler Tapes, Seals &amp; Gaskets.</li>
  <li>Boiler Close Up Kits.</li>
  <li>Welding Blankets, Curtains &amp; Screens</li>
</ul>
<ul class="abs chev-list prod-b">
  <li>Exhaust Thermal / Acoustic Covers.</li>
  <li>Thermal Hoods / Covers.</li>
  <li>Machine Thermal Covers.</li>
  <li>Thermal Fabrics.</li>
  <li>Thermal Fabrications - To your<br>Specification</li>
  <li>Fabric / Metallic Expansion Joints<br>&amp; Associated Metal Work</li>
</ul>

<section class="abs panel profile"><h3>Profile</h3></section>
<ul class="abs dot-list prof-a">
  <li>Folded Tape</li><li>Tadpole Tape</li><li>Glass Fibre Ropes</li><li>Glass Fibre</li><li>Square Braids</li><li>Welding Blankets</li><li>Injection</li>
</ul>
<ul class="abs dot-list prof-b">
  <li>Machine</li><li>Barrel Covers</li><li>Injection Machine</li><li>Nozzle Cover</li><li>Boat Exhaust</li><li>Covers</li><li>Valve Covers</li>
</ul>

<section class="abs panel testimonial">
  <h3>Testimonial</h3>
  <p>"Lorem ipsum dolor sit amet, consectetur adipiscing elit. Nam nec fringilla metus. Fusce non neque ante, eu lacinia diam. Pellentesque erat diam, suscipit et inter­dum eu, sodales vel odio."</p>
  <a href="#">Read More</a>
</section>

<div class="abs rule" style="top:1031px"></div>

<footer>
  <div class="abs footer-links">
    <a class="current" href="#">Home</a><span class="bar">|</span><a href="#">About Us</a><span class="bar">|</span><a href="#">Services</a><span class="bar">|</span><a href="#">Work</a><span class="bar">|</span><a href="#">Blog</a><span class="bar">|</span><a href="#">Contact Us</a>
  </div>
  <div class="abs footer-note" style="top:1075px">© Copyright 2011 Brightcoilheat. All Rights Reserved</div>
  <div class="abs footer-note small" style="top:1091px">Website Design &amp; Developed &nbsp;|&nbsp; SEO PPC Services : www.northlanestudio.com</div>
  <div class="abs footer-note small" style="top:1107px">Follow Us on &nbsp;: <span class="social"></span><span class="social"></span></div>
</footer>
</body>
</html>
```